Company corporate advertising sign and banner for different uses

Hello,
We are a handcraft business and in need of an advertising sign and banner for different uses based on our company logo.
The banner should be usable mainly for advertising on different websites and as this we think it should be in landscape format.
The advertising sign should be usable in different sizes. Firstly we would need it in 50cmx60cm or similar format, so we can let it print on plexiglas or as a plastic sign (and similar) to screw it on a wall near our company so people (mainly delivery companies) are able to find our warehouse on the other side we would need this same sign in plastic or perhaps thin metal to put it as an advertising and contact sign on our different projects that we are realizing, for example car barriers, video surveillance systems, alarm systems for home or company use (outside on the sirenes), on electric boxes like car charging stations, computers and much other things, so you see the very need that we must be able to change the size of the advertising sign but it must still be recognizable that our company realized that sort of work.
We have a logo that must be represented on that sign and also our company details must be present, so people are able to contact us.
The advertising sign and the banner should go hand in hand, so that everyone can recognize on first sight that it is our company.
We put our logo in the upload files section, the text on the right side of the logo can be used but is not an absolute must, depends on the ideas of the design and the designer.
The text we absolutely would need is beside our phone, website address and email address which are :
+352 27419586
www.plostermaak.lu
info@plostermaak.lu
the following text, representing our services :
Réparations et rénovations tout genre
Electricité générale, dépannages, domotique, systèmes d'alarme et de vidéosurveillance
Solutions et services en informatique
Aménagements de l'extérieur, services de jardinage
Thanks very much
Target Market(s)
private and business customers
Industry/Entity Type
craft business

```html
<!DOCTYPE html>
<html lang="fr">
<head>
<meta charset="utf-8">
<title>Plostermaak – panneaux et bannière</title>
<link rel="stylesheet" href="https://fonts.googleapis.com/css2?family=Montserrat:wght@600;700&family=Saira+Condensed:wght@800&display=swap">
<style>
  :root {
    --orange: #f5ad44;
    --navy: #22193a;
    --white: #ffffff;
    --frame: #cfcfcf;
  }
  * { box-sizing: border-box; margin: 0; padding: 0; }
  html, body { width: 1200px; height: 1200px; overflow: hidden; background: var(--white); }
  body { position: relative; }

  .sign {
    position: absolute;
    display: flex;
    flex-direction: column;
    border: 1px solid var(--frame);
    overflow: hidden;
  }
  .sign--light { left: 16px; top: 21px; width: 580px; height: 693px; --top: var(--white); --main: var(--orange); }
  .sign--warm  { left: 605px; top: 21px; width: 579px; height: 693px; --top: var(--orange); --main: var(--white); }
  .banner      { left: 16px; top: 723px; width: 1168px; height: 456px; --top: var(--white); --main: var(--orange); }

  .brand {
    background: var(--top);
    display: flex;
    align-items: center;
    justify-content: center;
    gap: 26px;
    flex: 0 0 231px;
  }
  .banner .brand { flex-basis: 202px; }
  .brand__mark { width: 118px; height: 118px; background: var(--navy); border-radius: 10px; }
  .banner .brand__mark { width: 126px; height: 126px; }
  .brand__name {
    font-family: "Montserrat", sans-serif;
    font-weight: 700;
    font-size: 32px;
    color: var(--navy);
    letter-spacing: 0.5px;
  }

  .rule { background: var(--navy); flex: 0 0 8px; }
  .gap-top { background: var(--top); flex: 0 0 7px; }
  .gap-main { background: var(--main); flex: 0 0 9px; }
  .banner .gap-top { flex-basis: 8px; }
  .banner .gap-main { flex-basis: 7px; }

  .services {
    background: var(--main);
    flex: 1 1 auto;
    display: flex;
    flex-direction: column;
    justify-content: center;
    align-items: center;
    text-align: center;
    font-family: "Saira Condensed", sans-serif;
    font-weight: 800;
    font-variant: small-caps;
    font-size: 25px;
    line-height: 45px;
    color: var(--navy);
    letter-spacing: 0.4px;
  }
  .banner .services { font-size: 26px; line-height: 45px; }

  .contact {
    background: var(--navy);
    color: var(--orange);
    font-family: "Montserrat", sans-serif;
    font-weight: 700;
    flex: 0 0 114px;
    display: flex;
    align-items: center;
    justify-content: space-between;
    padding: 0 20px 0 24px;
  }
  .contact__phone { font-size: 26px; }
  .contact__web { text-align: right; font-size: 26px; line-height: 36px; }
  .banner .contact { flex-basis: 59px; padding: 0 56px 0 52px; }
  .banner .contact span { font-size: 31px; }
</style>
</head>
<body>

<section class="sign sign--light">
  <div class="brand"><div class="brand__mark"></div><div class="brand__name">de Plostermaak</div></div>
  <div class="rule"></div><div class="gap-top"></div>
  <div class="services">
    <p>Réparations et rénovations tout genre</p>
    <p>Electricité générale, dépannages, domotique,</p>
    <p>systèmes d'alarme et de vidéosurveillance</p>
    <p>Solutions et services en informatique</p>
    <p>Aménagements de l'extérieur,</p>
    <p>services de jardinage</p>
  </div>
  <div class="rule"></div><div class="gap-main"></div>
  <div class="contact">
    <span class="contact__phone">+352 27419586</span>
    <div class="contact__web"><p>www.plostermaak.lu</p><p>info@plostermaak.lu</p></div>
  </div>
</section>

<section class="sign sign--warm">
  <div class="brand"><div class="brand__mark"></div><div class="brand__name">de Plostermaak</div></div>
  <div class="rule"></div><div class="gap-top"></div>
  <div class="services">
    <p>Réparations et rénovations tout genre</p>
    <p>Electricité générale, dépannages, domotique,</p>
    <p>systèmes d'alarme et de vidéosurveillance</p>
    <p>Solutions et services en informatique</p>
    <p>Aménagements de l'extérieur,</p>
    <p>services de jardinage</p>
  </div>
  <div class="rule"></div><div class="gap-main"></div>
  <div class="contact">
    <span class="contact__phone">+352 27419586</span>
    <div class="contact__web"><p>www.plostermaak.lu</p><p>info@plostermaak.lu</p></div>
  </div>
</section>

<section class="sign banner">
  <div class="brand"><div class="brand__mark"></div><div class="brand__name">de Plostermaak</div></div>
  <div class="rule"></div><div class="gap-top"></div>
  <div class="services">
    <p>Réparations et rénovations tout genre</p>
    <p>Electricité générale, dépannages, domotique, systèmes d'alarme et de vidéosurveillance</p>
    <p>Solutions et services en informatique Aménagements de l'extérieur, services de jardinage</p>
  </div>
  <div class="rule"></div><div class="gap-main"></div>
  <div class="contact">
    <span>+352 27419586</span>
    <span>www.plostermaak.lu</span>
    <span>info@plostermaak.lu</span>
  </div>
</section>

</body>
</html>
```